Australian Civil Construction, Quarry & Mining Services needs a business card

We need a business card designed for our Civil Construction, Quarry & Mining Services based in the country in Australia.
Our Company Brackley Earthworks provide innovate solutions for infrastructure, agricultural and mining (aggregate, sand, roadbase) industry.
We would like our business cards to be double sided
Front of card: black background or something that resembles our business colours. (it doesn't have to be black we are open to options)
- Company name - Brackley Earthworks
- Either our logo or some sort of icon/picture that resembles our business
- Website - https://brackleyearthworks.com.au/
- We will have a number of different names, positions descriptions, phone numbers and emails on separate cards for each of our managers/directors

```html
<!DOCTYPE html>
<html lang="en">
<head>
<meta charset="UTF-8">
<title>Brackley Earthworks – Business Card</title>
<link rel="stylesheet" href="https://fonts.googleapis.com/css2?family=Barlow:wght@400;500;600;700&family=Rajdhani:wght@700&display=swap">
<style>
  :root {
    --card-white: #ffffff;
    --ink-black: #151314;
    --brand-orange: #f5841c;
    --accent-orange: #dc5f17;
    --text-dark: #111111;
  }
  html, body {
    margin: 0;
    padding: 0;
    width: 1200px;
    height: 667px;
    overflow: hidden;
    background: var(--card-white);
  }
  .card {
    position: relative;
    width: 1200px;
    height: 667px;
    background: var(--card-white);
    overflow: hidden;
    font-family: "Barlow", Arial, sans-serif;
  }
  .brand-disc {
    position: absolute;
    left: 0;
    top: 0;
    width: 1200px;
    height: 667px;
  }
  .brand-name {
    position: absolute;
    left: 40px;
    top: 250px;
    width: 500px;
    margin: 0;
    text-align: center;
    font-family: "Barlow", Arial, sans-serif;
    font-weight: 700;
    font-size: 58px;
    line-height: 1.1;
    letter-spacing: 1px;
    text-transform: uppercase;
    color: var(--brand-orange);
  }
  .details {
    position: absolute;
    right: 29px;
    top: 0;
    text-align: right;
  }
  .company-title {
    margin: 54px 0 0;
    font-family: "Rajdhani", "Arial Narrow", sans-serif;
    font-weight: 700;
    font-size: 74px;
    line-height: 66px;
    letter-spacing: 3px;
    text-transform: uppercase;
    color: var(--text-dark);
  }
  .person-name {
    margin: 74px 0 0;
    font-weight: 500;
    font-size: 36px;
    line-height: 42px;
    color: var(--text-dark);
  }
  .person-role {
    margin: 2px 0 0;
    font-weight: 600;
    font-size: 36px;
    line-height: 42px;
    letter-spacing: 1px;
    color: var(--accent-orange);
  }
  .address {
    margin: 42px 0 0;
    font-style: normal;
    font-weight: 400;
    font-size: 28px;
    line-height: 43px;
    color: var(--text-dark);
  }
  .contact {
    margin: 44px 0 0;
    font-weight: 500;
    font-size: 28px;
    line-height: 43px;
    color: var(--accent-orange);
  }
  .contact p { margin: 0; }
</style>
</head>
<body>
  <main class="card">
    <svg class="brand-disc" viewBox="0 0 1200 667" aria-hidden="true">
      <circle cx="290" cy="340" r="312" fill="var(--ink-black)"/>
    </svg>
    <p class="brand-name">Brackley<br>Earthworks</p>

    <section class="details">
      <h1 class="company-title">Brackley<br>Earthworks</h1>
      <p class="person-name">First name Last Name</p>
      <p class="person-role">TITLE</p>
      <address class="address">
        42 Kellerman Road<br>
        Tallow Creek Victoria 3730<br>
        Australia
      </address>
      <div class="contact">
        <p class="contact-phone">Phone: 03 5712 0486</p>
        <p class="contact-email">Email: admin@brackleyearthworks.com.au</p>
      </div>
    </section>
  </main>
</body>
</html>
```